Call Center In Need of Website Design

We are a call center that provides inbound and outbound calling & marketing services for eCommerce store. We would like to see a fun, creative, playful design that is simple.

Here are some sample design sites we like;
- https://www.vorlintask.com/
- https://plumdesk.io/
- https://www.tandorix.com/live-chat-software/
- https://www.bexlora.com/

Here are some competitor sites;
- https://www.quillbranchlines.com/
- https://www.helpkestrel.com/

I have attached website content for your use.

Target Market(s)

eCommerce

Coding

Coded - Design and coding required

Number of Pages Required

5+ page

Font styles to use
Sans Serif

Colors

Designer to choose colors to be used in the design.

Requirements
Must have
• Must have designs for the following 5 separate pages;
• 1. Home (landing)
• - This will be were the design style really needs to show.
• - Just needs to touch on key services
• - CTA
• 2. About Us
• - Basic page for about me paragraph
• 3. Services
• - List of services with icons
• - Click on service type to expand details or hover over service icon to view popup bubble with details about that service
• 4. Pricing
• - Option to bundle 1(one) digital service plan and 1(one) call center service plan
• - Bundling adds 10% monthly discount to over all price
• - Customer does NOT have to bundle
• - FAQ
• 5. Contact Us
• - Include a capture form (name, company name, email, phone, message)
• - Contact info
• - Business hours
• When customer purchases their desired plan, then they are taken to a page where they must schedule a call with an account rep.
Nice to have
• home page animations
Should not have
• All information on Home/Landing page.

```html
<!DOCTYPE html>
<html lang="en">
<head>
<meta charset="utf-8">
<title>Corvana — Call Center &amp; Digital Services</title>
<link href="https://fonts.googleapis.com/css2?family=Poppins:wght@400;500&family=Arimo:wght@400&display=swap" rel="stylesheet">
<style>
:root{
  --teal:#52b89b;
  --teal-dark:#47a88c;
  --ink:#3c3c3c;
  --muted:#4a4a4a;
  --paper:#ffffff;
  --soft:#f4f4f4;
  --footer:#3b4747;
  --caption-dark:rgba(70,72,74,.82);
}
*{margin:0;padding:0;box-sizing:border-box}
html,body{width:902px;height:1200px;overflow:hidden;background:var(--paper)}
body{position:relative;font-family:'Poppins',sans-serif;color:var(--ink)}
.abs{position:absolute}

/* header */
.topline{left:0;top:0;width:902px;height:2px;background:var(--teal)}
.site-header{left:0;top:2px;width:902px;height:75px;background:var(--paper)}
.brand{display:flex;align-items:center;gap:10px}
.brand-dot{width:34px;height:34px;border:2px solid var(--teal);border-radius:50%}
.brand-name{font-family:'Poppins',sans-serif;font-weight:400;letter-spacing:4px;font-size:22px;color:#4a4a4a}
.site-header .brand{left:64px;top:22px}
.main-nav a{position:absolute;top:33px;font-size:10.5px;font-weight:500;color:#4a4a4a;text-decoration:none;white-space:nowrap}
.main-nav a.active{color:var(--teal)}

/* hero */
.hero{left:0;top:77px;width:902px;height:395px;background:linear-gradient(100deg,#8a6f5e 0%,#c9b7a6 35%,#b8aa9d 60%,#d9d2c8 100%)}
.hero-title{left:494px;top:304px;width:163px;height:46px;background:rgba(82,184,155,.88);color:#fff;font-size:26px;font-weight:500;padding-left:18px;line-height:46px;letter-spacing:.5px}
.hero-sub{left:494px;top:353px;width:381px;height:45px;background:var(--caption-dark);color:#fff;font-size:14px;font-weight:500;line-height:45px;padding-left:16px;white-space:nowrap}
.dots{left:432px;top:449px;display:flex;gap:3px}
.dots span{width:11px;height:11px;border:1.5px solid #555;border-radius:50%}
.dots span.on{border-color:#fff}

/* welcome */
.welcome{left:0;top:472px;width:902px;height:181px;background:var(--teal);text-align:center;color:#fff}
.welcome h1{font-weight:400;font-size:24px;margin-top:34px}
.rule{width:72px;height:2px;background:#fff;margin:10px auto 0}
.welcome p{font-family:'Arimo',Arial,sans-serif;font-size:9.6px;line-height:19.4px;width:570px;margin:9px auto 0}

/* services */
.services{left:0;top:653px;width:902px;height:430px;background:var(--soft);text-align:center}
.services h2{font-weight:400;font-size:22.5px;color:var(--teal);margin-top:26px}
.services .lead{font-family:'Arimo',Arial,sans-serif;font-size:9.6px;color:var(--muted);margin-top:6px}
.service{position:absolute;top:116px;width:290px;text-align:center}
.service-icon{margin:0 auto;width:96px;height:96px}
.service h3{font-weight:400;font-size:14.5px;color:var(--ink);margin-top:17px}
.service p{font-family:'Arimo',Arial,sans-serif;font-size:9.2px;line-height:19.4px;color:var(--muted);margin-top:9px}
.cta{left:368px;top:351px;width:166px;height:39px;border-radius:20px;background:var(--teal);color:#fff;font-size:14px;font-weight:500;line-height:39px;text-align:center}

/* footer */
.site-footer{left:0;top:1083px;width:902px;height:117px;background:var(--footer);color:#fff}
.site-footer .brand{left:101px;top:41px}
.site-footer .brand-name{color:#fff}
.foot-nav span{position:absolute;top:33px;font-size:10px;white-space:nowrap}
.copyright{left:375px;top:75px;font-family:'Arimo',Arial,sans-serif;font-size:9.2px}
.social{left:648px;top:67px;display:flex;gap:4px}
.social span{width:28px;height:28px;border:1.5px solid #fff;border-radius:50%}
</style>
</head>
<body>
<div class="abs topline"></div>

<header class="abs site-header">
  <div class="abs brand"><span class="brand-dot"></span><span class="brand-name">CORVANA</span></div>
  <nav class="main-nav">
    <a class="active" style="left:476px">HOME</a>
    <a style="left:538px">ABOUT US</a>
    <a style="left:621px">SERVICES</a>
    <a style="left:700px">PRICING</a>
    <a style="left:774px">CONTACT US</a>
  </nav>
</header>

<section class="abs hero" role="img" aria-label="Photo of smiling call center agents wearing headsets in an office"></section>
<div class="abs hero-title">CORVANA</div>
<div class="abs hero-sub">SED UT PERSPICIATIS UNDE OMNIS ISTE NATUS</div>
<div class="abs dots"><span></span><span class="on"></span><span></span></div>

<section class="abs welcome">
  <h1>Welcome to Our Company</h1>
  <div class="rule"></div>
  <p>Sed ut perspiciatis unde omnis iste natus error sit voluptatem accusantium doloremque laudantium, totam rem aperiam, eaque ipsa quae ab illo inventore veritatis et quasi architecto beatae vitae dicta sunt explicabo.Nemo enim ipsam voluptatem quia voluptas sit aspernatur aut odit aut fugit, sed quia consequuntur magni dolores eos qui ratione voluptatem sequi nesciunt.</p>
</section>

<section class="abs services">
  <h2>Our Services</h2>
  <p class="lead">Sed ut perspiciatis unde omnis iste natus error sit voluptatem accusantium doloremque laudantium, totam rem</p>

  <article class="service" style="left:106px">
    <svg class="service-icon" viewBox="0 0 96 96">
      <circle cx="48" cy="48" r="47" fill="none" stroke="var(--teal)" stroke-width="1.5"/>
      <circle cx="48" cy="48" r="42" fill="var(--teal)"/>
      <rect x="31" y="30" width="34" height="25" fill="none" stroke="#fff" stroke-width="2"/>
      <rect x="35" y="34" width="26" height="17" fill="none" stroke="#fff" stroke-width="1.2"/>
      <path d="M27 58h42v2H27z" fill="#fff"/>
      <path d="M41 40h3l7-4v12l-7-4h-3z" fill="none" stroke="#fff" stroke-width="1.3"/>
      <path d="M54 38l3-2M54 42h4M54 46l3 2" stroke="#fff" stroke-width="1.2"/>
    </svg>
    <h3>Digital Services</h3>
    <p>Sed ut perspiciatis unde omnis iste natus error sit voluptatem accusantium doloremque laudantium, totam rem aperiam, eaque architecto beatae vitae dicta sunt explicabo</p>
  </article>

  <article class="service" style="left:501px">
    <svg class="service-icon" viewBox="0 0 96 96">
      <circle cx="48" cy="48" r="47" fill="none" stroke="var(--teal)" stroke-width="1.5"/>
      <circle cx="48" cy="48" r="42" fill="var(--teal)"/>
      <path d="M30 50a18 18 0 0 1 36 0" fill="none" stroke="#fff" stroke-width="3"/>
      <rect x="27" y="46" width="7" height="12" rx="3" fill="#fff"/>
      <rect x="62" y="46" width="7" height="12" rx="3" fill="#fff"/>
      <path d="M36 58q6 8 12 6" fill="none" stroke="#fff" stroke-width="2"/>
      <circle cx="49" cy="64" r="2.5" fill="#fff"/>
    </svg>
    <h3>Call Center Services</h3>
    <p>Sed ut perspiciatis unde omnis iste natus error sit voluptatem accusantium doloremque laudantium, totam rem aperiam, eaque architecto beatae vitae dicta sunt explicabo</p>
  </article>

  <div class="abs cta">Get A Request</div>
</section>

<footer class="abs site-footer">
  <div class="abs brand"><span class="brand-dot"></span><span class="brand-name">CORVANA</span></div>
  <nav class="foot-nav">
    <span style="left:375px">HOME</span><span style="left:427px">|</span>
    <span style="left:455px">ABOUT US</span><span style="left:526px">|</span>
    <span style="left:554px">SERVICES</span><span style="left:622px">|</span>
    <span style="left:650px">PRICING</span><span style="left:712px">|</span>
    <span style="left:739px">CONTACT US</span>
  </nav>
  <p class="abs copyright">© Copyright-2018 Corvana.All rights reserved.</p>
  <div class="abs social" aria-label="Social links"><span></span><span></span><span></span><span></span><span></span></div>
</footer>
</body>
</html>
```